Construction Company - Aluminum Welding Substations - 8 page Brochure

See attached for very rough idea of brochure idea and general idea - primary goal is to highlight various services provided as unique for our industry.

- About Us - see website (brevoforge.com) & Company Resume

- Why Welded Fittings - see PPT & language in comments

- Services Provided - See categories broke out on website - highlight Aluminum Bus Welding, Bus Bending, All Weather Welding, Field Fabrication.

- Contact Page - see website

- Want to use as many photo's to highlight work as possible as people like to see the finished product of the substation/bus bending
Updates

Target Market(s)

General Contractors - we are Specialty Subcontractor

Industry/Entity Type

Construction - Welding Substations

Font styles to use
Serif
Sans Serif

Colors
0054AA
0677BA
7BADD7
CADEEF
E8F1F8
0094D4
00A9DD
6FCCEA
C7EBF8
E9F6FB
F0912C
F2A743
F7CA91
FBE8D2
FDF5EE

Requirements
Must have
• Logo, "Quality Craftsmanship without Compromise", Services Provided, as many pictures as makes sense to highlight work

```html
<!DOCTYPE html>
<html lang="en">
<head>
<meta charset="utf-8">
<title>Brevo Forge Brochure – Pages 4–5</title>
<link rel="stylesheet" href="https://fonts.googleapis.com/css2?family=Poppins:ital,wght@0,400;0,500;0,600;0,700;0,800;1,700;1,800&display=swap">
<style>
  :root{
    --navy:#1d2760;
    --navy-deep:#18204f;
    --navy-mid:#27347f;
    --teal:#2ca6c4;
    --teal-light:#6fcbe2;
    --ink:#2f2f33;
    --page-light:#efefef;
    --page-mid:#d9dadb;
    --photo-border:#ffffff;
    --sky:#3f7fc6;
    --sky-light:#a9c7e6;
    --steel:#8e9aa8;
    --gravel:#b7b9bc;
    --text-on-dark:#e3e7f3;
  }
  *{box-sizing:border-box;margin:0;padding:0}
  html,body{width:1200px;height:700px;overflow:hidden;background:#aecfd1}
  body{font-family:"Poppins",sans-serif;color:var(--ink)}
  .spread{position:relative;width:1200px;height:700px;display:flex}
  .page{position:relative;width:600px;height:700px;overflow:hidden}
  .page--left{background:linear-gradient(180deg,var(--page-light) 0%,#e4e5e6 55%,var(--page-mid) 100%)}
  .page--right{background:linear-gradient(135deg,var(--navy-mid) 0%,var(--navy) 45%,var(--navy-deep) 100%)}
  .page__spine{position:absolute;top:0;left:598px;width:4px;height:700px;background:rgba(0,0,0,.12);z-index:5}

  .content{position:absolute;left:34px;top:46px;width:300px}
  .eyebrow{font-size:11px;font-weight:700;color:var(--teal)}
  .title{font-size:17px;font-weight:800;color:var(--navy);margin-top:2px}
  .rule{display:flex;gap:4px;margin:6px 0 12px}
  .rule span{height:3px;border-radius:2px}
  .rule .rule__teal{width:44px;background:var(--teal)}
  .rule .rule__navy{width:34px;background:var(--navy)}
  .section{font-size:10.5px;font-weight:800;font-style:italic;color:var(--teal);text-transform:uppercase;margin:8px 0 4px;letter-spacing:.2px}
  .list{list-style:none}
  .list li{position:relative;padding-left:13px;font-size:8.6px;line-height:1.3;margin-bottom:5px}
  .list li::before{content:"";position:absolute;left:1px;top:3px;border-left:5px solid var(--teal);border-top:3px solid transparent;border-bottom:3px solid transparent}
  .list strong{font-weight:700;color:#1c1c20}
  .caps{text-transform:uppercase}

  .footer{position:absolute;bottom:34px;font-size:10px;display:flex;align-items:center;gap:14px}
  .footer .page-no{font-weight:700}
  .footer .url b{font-weight:700}
  .page--left .footer{left:34px;color:#3a3a3e}
  .page--right .footer{right:30px;color:var(--text-on-dark)}

  .photo{position:absolute;border:4px solid var(--photo-border);box-shadow:0 2px 6px rgba(0,0,0,.25)}
  .photo--sky{background:linear-gradient(180deg,var(--sky) 0%,var(--sky-light) 60%,var(--steel) 100%)}
  .photo--work{background:linear-gradient(180deg,#c9d6e3 0%,#8897a6 50%,#54565c 100%)}
  .photo--yard{background:linear-gradient(180deg,#2f5f9f 0%,#6d8fb5 50%,#3a3f48 100%)}
  .backdrop{position:absolute;background:linear-gradient(180deg,#dfe6ef 0%,#bfc4ca 55%,var(--gravel) 100%);opacity:.75}

  .right-backdrop{position:absolute;left:0;top:0;width:330px;height:700px;background:linear-gradient(90deg,#6f7f95 0%,#42557f 60%,rgba(29,39,96,0) 100%);opacity:.85}

  .concerns{position:absolute;left:300px;top:70px;width:272px;color:var(--text-on-dark)}
  .concerns .title{color:var(--teal-light);font-size:13px;font-weight:700}
  .concerns .rule .rule__teal{width:40px;background:var(--teal-light)}
  .concerns .rule .rule__navy{width:26px;background:#fff}
  .concerns .section{color:var(--teal-light);font-size:9.5px;margin-top:6px}
  .concerns .list li{font-size:7.6px;margin-bottom:3px}
  .concerns .list li::before{border-left-color:var(--teal-light)}
  .sub{font-weight:700;font-size:8px;color:#fff}
  .sub-text{list-style:none;padding-left:12px;margin:2px 0 4px}
  .sub-text li{font-size:7.4px;line-height:1.35;margin-bottom:2px}
  .sub-text li::before{display:none}
</style>
</head>
<body>
<div class="spread">

  <section class="page page--left">
    <div class="backdrop" style="left:300px;top:0;width:300px;height:700px" role="img" aria-label="Faded photo of a substation yard with gravel ground"></div>

    <div class="content">
      <p class="eyebrow">Why Welded Fittings</p>
      <h2 class="title">Why Welded Connectors?</h2>
      <div class="rule"><span class="rule__teal"></span><span class="rule__navy"></span></div>

      <h3 class="section">IPSE – Prefered Method:</h3>
      <ul class="list">
        <li>Per IPSE 6.6.1.4, Welded connectors are the preferred method of bus and cable installation in power substations.</li>
        <li>Per IPSE 6.6.1.2 Compression fittings are intended to be installed on stranded conductors. Compressed should be oriented down to prevent the entrance of moisture into the connection.</li>
      </ul>

      <h3 class="section">Reliability/Low Resistance:</h3>
      <ul class="list">
        <li>Forms a SOLID, homogeneous connection.</li>
        <li>Excellent structural, mechanical and electrical performance with <strong>NO CONTACT RESISTANCE (IPSE)</strong></li>
        <li>Cascade power administration did a study on welded substations and connectors and found that in the case of a seismic event welding creates a <strong>SEISMICLY SUPERIOR</strong> overall substation, when welded properly.</li>
        <li>No risk of <strong>EXPANSION OR CONTRACTION</strong></li>
        <li><strong>LESS CHANCE OF CORONA</strong> in high voltage EHV and UHV applications – keeping the profile smooth.</li>
      </ul>

      <h3 class="section">Cost Savings:</h3>
      <ul class="list">
        <li><span class="caps">Parts</span> are generally <span class="caps">less expensive</span> than bolted or compression fittings.</li>
        <li><span class="caps">Faster installation</span> – only need one welder per connection vs. multiple laborers for bolted or compression fittings.</li>
        <li>Time savings with the <span class="caps">ability for pre-fab</span> on the ground for future installation, that coincides with other job phases.</li>
        <li>When performed in conjunction with <span class="caps">bus bending creates additional savings</span> of material, labor and overall installation time.</li>
        <li>Time and cost savings due to <span class="caps">adaptability</span> in the field.</li>
      </ul>
    </div>

    <div class="photo photo--sky" style="left:348px;top:70px;width:128px;height:170px" role="img" aria-label="Photo of welded aluminum bus structure against a blue sky"></div>
    <div class="photo photo--sky" style="left:480px;top:60px;width:118px;height:150px" role="img" aria-label="Photo of a bucket lift working on a substation"></div>
    <div class="photo photo--yard" style="left:400px;top:196px;width:160px;height:110px" role="img" aria-label="Photo of a completed substation bus yard"></div>
    <div class="photo photo--work" style="left:348px;top:300px;width:160px;height:220px" role="img" aria-label="Photo of a welder working on aluminum bus from a lift"></div>
    <div class="photo photo--sky" style="left:506px;top:310px;width:94px;height:110px" role="img" aria-label="Photo of lifts raised beside substation structures"></div>

    <footer class="footer"><span class="page-no">Page 4</span><span>|</span><span class="url">www.<b>brevoforge</b>.com</span></footer>
  </section>

  <div class="page__spine"></div>

  <section class="page page--right">
    <div class="right-backdrop" role="img" aria-label="Faded photo of stacked aluminum bus pipe in a substation yard"></div>

    <div class="photo photo--sky" style="left:12px;top:60px;width:96px;height:260px" role="img" aria-label="Photo of a crew truck parked beside a substation frame"></div>
    <div class="photo photo--work" style="left:100px;top:240px;width:110px;height:170px" role="img" aria-label="Photo of welded bus fittings on insulators"></div>

    <div class="concerns">
      <h2 class="title">Common Concerns</h2>
      <div class="rule"><span class="rule__teal"></span><span class="rule__navy"></span></div>

      <h3 class="section">Finding Aluminum Welders:</h3>
      <ul class="list">
        <li>All BF Welders are AWQ certified for both steel and aluminum. CPA Certified for both MIG and TIG</li>
        <li>Directly trained in high voltage substations</li>
        <li>Perform in-house training – high internal quality control standards.</li>
        <li>Niche/Specialty – Perform this work everyday, creates inherent efficiencies.</li>
        <li>Currently have 11 fully outfitted welding trucks</li>
        <li>Currently Licensed in 8 states</li>
        <li>Continuously expanding our work force and territory</li>
      </ul>

      <h3 class="section">Safety/Quality/Efficiency</h3>
      <ul class="list">
        <li><span class="sub">Safety:</span></li>
      </ul>
      <ul class="sub-text"><li>Never had a recordable Safety Incident – EMR Rating of .77</li></ul>
      <ul class="list">
        <li><span class="sub">Quality:</span></li>
      </ul>
      <ul class="sub-text">
        <li>Company Culture Emphasizes Quality – its one of our core values</li>
        <li>Company Moto: "Quality Craftsmanship without Compromise"</li>
        <li>Customer Satisfaction – Standard = Every customer/every time</li>
      </ul>
      <ul class="list">
        <li><span class="sub">Efficiency:</span></li>
      </ul>
      <ul class="sub-text">
        <li>One stop shop – perform layout, cutting, fitting, prefab, arial installation, routing of bus, troubleshooting.</li>
        <li>"Be part of the solution, not part of the problem" – Core Value</li>
        <li>No wasted movements – everything we do has a purpose</li>
      </ul>
    </div>

    <footer class="footer"><span class="page-no">Page 5</span><span>|</span><span class="url">www.<b>brevoforge</b>.com</span></footer>
  </section>

</div>
</body>
</html>
```